Willowmere Loft B&B Business Card

This beautiful high-class B&B is looking for a business card that stands out from the rest. They are in the middle of the countryside, have chickens, geese and a dog. They also love bumble bees.

I was maybe thinking a rustic drawing / print of a bumble bee and a sketch of the house, I am not sure.. I quite like the feel of this... http://www.tarnwick-mill.co.uk/

Industry/Entity Type

Business

Contact Information for Business Card

Willowmere Loft
Bed & Breakfast
Brackleford, Hensworth, Somerset, TA14 7QP
01632 960418 | www.willowmereloft.co.uk

```html
<!DOCTYPE html>
<html lang="en">
<head>
<meta charset="utf-8">
<title>Willowmere Loft B&amp;B Business Card</title>
<link href="https://fonts.googleapis.com/css2?family=Mulish:wght@400;600;800&display=swap" rel="stylesheet">
<style>
  :root {
    --backdrop: #e9e6e1;
    --navy-deep: #0e3566;
    --navy-light: #2b5a88;
    --gold: #c9862c;
    --gold-soft: #b8782a;
    --ink-light: #ffffff;
  }
  html, body {
    margin: 0;
    width: 1200px;
    height: 900px;
    overflow: hidden;
    background: var(--backdrop);
    font-family: "Mulish", "Century Gothic", sans-serif;
  }
  .stage {
    position: relative;
    width: 1200px;
    height: 900px;
  }
  .card {
    position: absolute;
    left: 320px;
    width: 560px;
    height: 320px;
    background: linear-gradient(100deg, var(--navy-deep) 0%, var(--navy-light) 100%);
    box-shadow: 0 10px 24px rgba(0,0,0,0.25);
    box-sizing: border-box;
  }
  .card-front { top: 110px; }
  .card-back { top: 470px; }

  .front-frame {
    position: absolute;
    inset: 18px;
    border: 2px solid var(--gold);
  }
  .brand {
    position: absolute;
    top: 62px;
    left: 0;
    right: 0;
    text-align: center;
  }
  .brand-name {
    margin: 0;
    color: var(--gold);
    font-weight: 800;
    font-size: 34px;
    letter-spacing: 3px;
    line-height: 1;
  }
  .brand-rule {
    width: 390px;
    height: 2px;
    margin: 7px auto 6px;
    background: var(--ink-light);
  }
  .brand-tagline {
    margin: 0;
    color: var(--gold);
    font-weight: 800;
    font-size: 30px;
    letter-spacing: 1.5px;
    line-height: 1;
  }
  .contact-list {
    position: absolute;
    top: 178px;
    left: 0;
    right: 0;
    margin: 0;
    padding: 0;
    list-style: none;
    text-align: center;
    color: var(--ink-light);
    font-size: 15px;
    letter-spacing: 0.6px;
  }
  .contact-list li {
    display: flex;
    justify-content: center;
    align-items: center;
    gap: 7px;
    height: 24px;
  }
  .contact-icon {
    width: 15px;
    height: 15px;
    fill: var(--gold);
  }

  .house-sketch {
    position: absolute;
    left: 62px;
    top: 38px;
    width: 436px;
    height: 200px;
    background: linear-gradient(90deg, rgba(201,134,44,0.55), rgba(184,120,42,0.8));
  }
  .back-web {
    position: absolute;
    right: 56px;
    bottom: 34px;
    color: var(--gold);
    font-weight: 800;
    font-size: 19px;
    letter-spacing: 1.2px;
    padding-bottom: 5px;
    border-bottom: 2px solid var(--gold);
  }
</style>
</head>
<body>
<main class="stage">

  <section class="card card-front">
    <div class="front-frame"></div>
    <header class="brand">
      <h1 class="brand-name">WILLOWMERE LOFT</h1>
      <div class="brand-rule"></div>
      <p class="brand-tagline">Bed &amp; Breakfast</p>
    </header>
    <ul class="contact-list">
      <li>
        <svg class="contact-icon" viewBox="0 0 16 16" aria-hidden="true"><path d="M2 5c0-2 2-3 6-3s6 1 6 3v1h-3V5H5v1H2z M4 7h8l2 6H2z"/><circle cx="8" cy="10" r="1.6" fill="#1a4577"/></svg>
        <span>01632 960418</span>
      </li>
      <li>
        <svg class="contact-icon" viewBox="0 0 16 16" aria-hidden="true"><circle cx="8" cy="8" r="7"/><path d="M1 8h14M8 1v14M8 1c-3 3-3 11 0 14M8 1c3 3 3 11 0 14M2.5 4.5h11M2.5 11.5h11" stroke="#1a4577" stroke-width="1" fill="none"/></svg>
        <span>www.willowmereloft.co.uk</span>
      </li>
      <li>
        <svg class="contact-icon" viewBox="0 0 16 16" aria-hidden="true"><path d="M8 1L0 8h2v7h4v-4h4v4h4V8h2z"/></svg>
        <span>Brackleford, Hensworth, Somerset, TA14 7QP</span>
      </li>
    </ul>
  </section>

  <section class="card card-back">
    <div class="house-sketch" role="img" aria-label="Gold print-style sketch of the barn house with its pitched roof and garden shrubs"></div>
    <div class="back-web">www.willowmereloft.co.uk</div>
  </section>

</main>
</body>
</html>
```